Water Filter Company Needs Bizz Cards!!

Need business cards for my company. We sell whole home water filters and salt free water softeners. No more buying bottled water. Our filtering units filter out all heavy metals, chlorine, and VOC's, last 15 years, and are maintenance free and supply your whole home with spring quality alkaline water. Our Salt free water conditioners, eliminate hard water and scale, without lowering the ph, or TDS's (total Dissolved solids)

I think this is the color code we are using on my site. My logo looks good behind it. #192841

Website will be www.Brovexa.com

Industry/Entity Type

Water Purification

Contact Information for Business Card

For now, just insert standard Dummy text. I need these text lines for the info to be editable so i can make them for multiple employees. I do have Photoshop and illustrator, unless there is a simpler program i can use solely for biz cards

Font styles to use
Sans Serif

Requirements
Must have
• Use my preexisting logo.

www.BroVexa.com

Spring Quality Alkaline Water at every tap.

List out services. Whole Home Water Filters, Salt Free Water Softeners, Clarimont KT7, UV Sterilizers
Nice to have
• I think this is the color code we are using on my site. My logo looks good behind it. #192841 or black. Please no white or light blue backgrounds.

Maybe a picture of my tank.

Slogan like Spring Quality Alkaline Water at every tap.
And just list the services Whole Home Water Filters, Salt Free Water Softeners, Clarimont KT7, UV Sterilizers

I think I would like to not have a contrasting textured logo like I see on some of them. I may use it for my personal cards, but new employees may not want the extra expense.
Should not have
• A different logo than the one provided.

White or baby blue backgrounds. Use the color code, or blacks.

```html
<!DOCTYPE html>
<html lang="en">
<head>
<meta charset="utf-8">
<title>Brovexa Business Cards</title>
<link href="https://fonts.googleapis.com/css2?family=Josefin+Sans:wght@300;400;600&display=swap" rel="stylesheet">
<style>
  :root {
    --bg: #e6e6e6;
    --navy: #192841;
    --navy-back: #16223b;
    --brand-blue: #3fa9dc;
    --deep-blue: #0a7cc4;
    --water-light: #6cc0ea;
    --soft-text: #c3c9d4;
    --muted-text: #9aa3b2;
    --grey-band: #b9b9b9;
    --white: #ffffff;
  }
  * { margin: 0; padding: 0; box-sizing: border-box; }
  html, body { width: 1200px; height: 1200px; overflow: hidden; }
  body {
    background: var(--bg);
    font-family: "Josefin Sans", sans-serif;
    position: relative;
  }
  .card {
    position: absolute;
    left: 227px;
    width: 746px;
    height: 425px;
    border-radius: 38px;
    overflow: hidden;
  }
  .card-front { top: 135px; background: var(--navy); }
  .card-back { top: 640px; background: var(--navy-back); }

  .water-splash {
    position: absolute;
    left: 0; top: 0;
    width: 140px; height: 425px;
    background: linear-gradient(160deg, var(--water-light) 0%, var(--deep-blue) 55%, var(--brand-blue) 100%);
    clip-path: polygon(0 0, 78px 0, 70px 120px, 95px 230px, 130px 320px, 125px 425px, 0 425px);
  }

  .brand-lockup {
    position: absolute;
    display: flex;
    align-items: center;
    gap: 18px;
  }
  .brand-lockup .brand-dot {
    width: 46px; height: 46px;
    border-radius: 50%;
    background: var(--brand-blue);
  }
  .brand-lockup .brand-name {
    font-weight: 600;
    color: var(--brand-blue);
    letter-spacing: -1px;
    line-height: 1;
  }
  .card-front .brand-lockup { left: 108px; top: 42px; }
  .card-front .brand-name { font-size: 78px; }
  .card-back .brand-lockup { left: 0; right: 0; top: 160px; justify-content: center; }
  .card-back .brand-name { font-size: 84px; }
  .card-back .brand-dot { width: 52px; height: 52px; }

  .slogan {
    position: absolute;
    left: 183px; top: 124px;
    font-size: 15px; font-weight: 400;
    letter-spacing: 0.6px;
    color: var(--brand-blue);
    white-space: nowrap;
  }

  .person { position: absolute; left: 187px; top: 176px; }
  .person-name { font-size: 25px; font-weight: 400; color: var(--brand-blue); }
  .person-role { font-size: 18px; font-weight: 300; color: var(--muted-text); margin-top: 6px; }

  .contact-list {
    position: absolute; left: 187px; top: 263px;
    list-style: none;
  }
  .contact-list li {
    display: flex; align-items: center; gap: 12px;
    font-size: 18px; font-weight: 300; color: var(--soft-text);
    height: 25.5px;
  }
  .contact-icon { width: 17px; height: 17px; flex: none; }

  .service-list {
    position: absolute; left: 465px; top: 238px;
    list-style: none;
  }
  .service-list li {
    display: flex; align-items: center; gap: 12px;
    font-size: 18px; font-weight: 300; color: var(--soft-text);
    height: 24.8px;
  }
  .service-bullet {
    width: 10px; height: 10px; border-radius: 50%;
    background: var(--brand-blue); flex: none;
  }

  .address-band {
    position: absolute; left: 124px; top: 357px;
    width: 537px; height: 41px;
    background: linear-gradient(90deg, var(--brand-blue), var(--deep-blue));
    display: flex; align-items: center;
    padding-left: 61px;
    color: var(--white); font-size: 18px; font-weight: 300;
  }
  .address-band-end {
    position: absolute; left: 661px; top: 357px;
    width: 85px; height: 41px;
    background: var(--grey-band);
  }
</style>
</head>
<body>

<section class="card card-front">
  <div class="water-splash" role="img" aria-label="Photo of splashing water with bubbles"></div>

  <div class="brand-lockup">
    <span class="brand-dot"></span>
    <span class="brand-name">Brovexa</span>
  </div>
  <p class="slogan">Spring Quality Alkaline Water at every tap.</p>

  <div class="person">
    <p class="person-name">Daniel Hartwell</p>
    <p class="person-role">Managing Director</p>
  </div>

  <ul class="contact-list">
    <li>
      <svg class="contact-icon" viewBox="0 0 20 20" aria-hidden="true">
        <circle cx="10" cy="10" r="10" fill="#3fa9dc"/>
        <path d="M5 8 Q10 4 15 8 L13.5 9.5 L12 8.5 L8 8.5 L6.5 9.5 Z M7 10 H13 L14 14 H6 Z" fill="#fff"/>
      </svg>
      <span>(55) 0198 765 432</span>
    </li>
    <li>
      <svg class="contact-icon" viewBox="0 0 20 20" aria-hidden="true">
        <circle cx="10" cy="10" r="10" fill="#3fa9dc"/>
        <rect x="5" y="6.5" width="10" height="7" fill="none" stroke="#fff" stroke-width="1.3"/>
        <path d="M5 6.5 L10 11 L15 6.5" fill="none" stroke="#fff" stroke-width="1.3"/>
      </svg>
      <span>info@brovexa.com</span>
    </li>
    <li>
      <svg class="contact-icon" viewBox="0 0 20 20" aria-hidden="true">
        <circle cx="10" cy="10" r="10" fill="#3fa9dc"/>
        <circle cx="10" cy="10" r="5.5" fill="none" stroke="#fff" stroke-width="1.2"/>
        <path d="M4.5 10 H15.5 M10 4.5 Q6.5 10 10 15.5 M10 4.5 Q13.5 10 10 15.5" fill="none" stroke="#fff" stroke-width="1"/>
      </svg>
      <span>www.brovexa.com</span>
    </li>
  </ul>

  <ul class="service-list">
    <li><span class="service-bullet"></span>Whole home water filters</li>
    <li><span class="service-bullet"></span>Salt free water softeners</li>
    <li><span class="service-bullet"></span>Clarimont KT7</li>
    <li><span class="service-bullet"></span>UV Sterilizers</li>
  </ul>

  <div class="address-band">4827 Harbor Lane, Riverton, USA</div>
  <div class="address-band-end"></div>
</section>

<section class="card card-back">
  <div class="brand-lockup">
    <span class="brand-dot"></span>
    <span class="brand-name">Brovexa</span>
  </div>
</section>

</body>
</html>
```